Website - Tides Of Bloom

We are catalysts of change in people's lives.
We work with individuals and professionals to bring about instant substantial & transforming change in their lives.
We provide one-on-one lifestyle coaching by an experienced practitioner.
Our existing website is www.tidesofbloom.biz & this site contains our the basis for the content of our desired new project, so please examine this carefully.
We require a professional and captivating website that will instantly impress, engage invite our readers to click & invest their lives.
Our services do not come cheap, but are second to none.
Our website must be contemporary whilst reflecting indisputable class & ultra-confidence in the success of our work.
Target Market(s)
Those who seek to want to change in their lives. Those aged primarily between 30 and 50 years of age, male or female.
Industry/Entity Type
Work
Look and feel

```html
<!DOCTYPE html>
<html lang="en">
<head>
<meta charset="utf-8">
<title>Tides Of Bloom</title>
<link href="https://fonts.googleapis.com/css2?family=Roboto+Condensed:wght@300;400;700&family=Open+Sans:wght@400;600&family=Tinos&family=Arimo:ital,wght@0,400;1,400;1,700&display=swap" rel="stylesheet">
<style>
:root{
  --black:#000;
  --ink:#1a1a1a;
  --grey-text:#666;
  --light-grey:#bbb;
  --orange:#f36f21;
  --orange-text:#ff7a1a;
  --green:#8cc63f;
  --green-light:#b6e36e;
  --blue:#55b8e6;
  --hero-bg:#ececec;
  --footer-bg:#3a3a3a;
  --rule:#bfbfbf;
}
*{margin:0;padding:0;box-sizing:border-box}
html,body{width:1200px;height:1132px;overflow:hidden;background:#fff}
body{position:relative;font-family:'Roboto Condensed',sans-serif}
.abs{position:absolute}
.site-header{left:0;top:0;width:1200px;height:160px;background:var(--black)}
.brand{left:195px;top:40px;display:flex;align-items:center;gap:18px}
.brand-mark{width:26px;height:26px;background:var(--orange)}
.brand-name{font-family:'Roboto Condensed',sans-serif;font-weight:700;font-size:46px;color:#9a9a9a;line-height:1}
.call{left:776px;top:42px;color:#fff}
.call-label{position:absolute;left:50px;top:4px;font-family:'Open Sans',sans-serif;font-size:17px;color:#ddd;white-space:nowrap}
.call-number{position:absolute;left:47px;top:20px;font-family:'Open Sans',sans-serif;font-size:30px;white-space:nowrap}
.call-note{position:absolute;left:51px;top:56px;font-size:15px;color:#ccc;font-weight:300;white-space:nowrap}
.nav{left:0;top:160px;width:1200px;height:40px;background:var(--black);border-top:1px solid #333}
.nav a{position:absolute;top:8px;font-size:19px;color:var(--orange);text-decoration:none}
.nav a.active{border-top:3px solid var(--green);top:0;padding:6px 7px 0}
.hero{left:0;top:200px;width:1200px;height:407px;background:var(--hero-bg)}
.hero-title{left:182px;top:212px;font-family:'Tinos',serif;color:var(--black);line-height:1}
.hero-title .big{font-size:90px;letter-spacing:1px}
.hero-title .sub{font-size:41px;margin-left:8px;margin-top:-6px}
.hero-rule{left:185px;top:341px;width:421px;height:1px;background:#999}
.benefits{left:193px;top:375px;list-style:none}
.benefits li{font-size:19px;color:var(--grey-text);height:37px;display:flex;align-items:center;gap:10px;font-weight:300}
.tag{width:28px;height:14px;clip-path:polygon(0 0,80% 0,100% 50%,80% 100%,0 100%)}
.btn{top:522px;height:47px;border-radius:6px;font-size:19px;color:#222;display:flex;align-items:center;justify-content:center}
.btn-learn{left:191px;width:144px;background:linear-gradient(#ffd67a,#f9b23a);border:1px solid #e0962a}
.btn-get{left:341px;width:144px;background:linear-gradient(#7fd0f5,#3fa6e0);border:1px solid #2f8cc4}
.hero-photo{left:655px;top:205px;width:370px;height:402px;background:radial-gradient(ellipse at 60% 45%,#d9d4cf 0,#b9b3ae 40%,rgba(236,236,236,0) 72%)}
.band{left:0;top:607px;width:1200px;height:100px;background:linear-gradient(var(--green-light),var(--green));font-family:'Tinos',serif;font-size:32px;color:var(--ink);display:flex;align-items:center;justify-content:center;word-spacing:2px}
.band span{margin:0 14px}
.section-title{left:186px;top:718px;width:829px;text-align:center;font-size:24px;color:var(--ink);padding-bottom:8px;border-bottom:1px solid var(--rule)}
.intro{left:198px;top:768px;width:800px;font-size:15.5px;line-height:19px;color:var(--grey-text)}
.intro p+p{margin-top:18px}
.intro .hl{color:var(--orange)}
.rule2{left:186px;top:900px;width:829px;height:1px;background:var(--rule)}
.testi-title{left:194px;top:909px;font-size:22px;font-weight:700;color:var(--orange-text)}
.arrows{left:985px;top:908px;display:flex;gap:2px}
.arrows span{width:14px;height:14px;background:#111;color:#fff;font-size:10px;display:flex;align-items:center;justify-content:center}
.testi{top:940px;width:270px;height:50px;font-family:'Arimo',sans-serif}
.testi .avatar{position:absolute;left:4px;top:2px;width:45px;height:46px;background:linear-gradient(#c9b8a8,#6d5d52)}
.testi .name{position:absolute;left:62px;top:0;font-size:11px;font-weight:700;font-style:italic;color:#222}
.testi .quote{position:absolute;left:62px;top:12px;width:200px;font-size:8.5px;font-style:italic;line-height:10px;color:#444}
.testi .time{position:absolute;left:63px;top:41px;font-size:8.5px;color:#222}
.footer{left:0;top:1015px;width:1200px;height:117px;background:var(--footer-bg)}
.f-contact{left:188px;top:1025px;color:#fff;font-size:15px}
.f-contact small{display:block;font-size:11.5px;color:var(--light-grey);line-height:15px;margin-top:2px;font-weight:300}
.socials{left:519px;top:1039px;display:flex;gap:11px}
.socials span{width:35px;height:35px;border:2px solid #666;border-radius:50%}
.f-call{left:817px;top:1025px;color:#fff;font-family:'Open Sans',sans-serif}
.f-call .l{font-size:17px;color:#bbb;margin-left:3px}
.f-call .n{font-size:29px;line-height:30px}
.f-rule{left:220px;top:1100px;width:760px;height:1px;background:linear-gradient(90deg,transparent,#555,transparent)}
.copyright{left:0;top:1113px;width:1200px;text-align:center;font-family:'Open Sans',sans-serif;font-size:9.5px;color:#ddd}
</style>
</head>
<body>
<header class="site-header abs"></header>
<div class="brand abs"><span class="brand-mark"></span><span class="brand-name">Tides Of Bloom</span></div>
<div class="call abs">
  <svg width="44" height="44" viewBox="0 0 44 44"><circle cx="22" cy="22" r="19" fill="none" stroke="#f36f21" stroke-width="3"/><path d="M15 13c2-1 4 3 4 4s-2 2-1 4 3 4 5 4c1 0 2-2 3-1s4 3 3 5c-1 2-4 3-7 2s-8-6-9-11c0-3 1-6 2-7z" fill="none" stroke="#f36f21" stroke-width="2.2"/></svg>
  <span class="call-label">CALL TOLL-FREE</span>
  <span class="call-number">1-800-555-0137</span>
  <span class="call-note">24/7 Support -Call at any time</span>
</div>
<nav class="nav abs">
  <a class="active" href="#" style="left:706px">Home</a>
  <a href="#" style="left:782px">Business</a>
  <a href="#" style="left:868px">Individual</a>
  <a href="#" style="left:957px">Contact</a>
</nav>

<section class="hero abs"></section>
<h1 class="hero-title abs"><div class="big">CHANGE</div><div class="sub">IS YOURS LIFE STYLE</div></h1>
<div class="hero-rule abs"></div>
<ul class="benefits abs">
  <li><span class="tag" style="background:#5bbfd0"></span>More choices about your behaviours and emotions</li>
  <li><span class="tag" style="background:var(--orange)"></span>Improve your relationships and the ways you communicate</li>
  <li><span class="tag" style="background:var(--green)"></span>Create better results through becoming a greater thinker</li>
</ul>
<a class="btn btn-learn abs">Learn More</a>
<a class="btn btn-get abs">Get It Now</a>
<div class="hero-photo abs" role="img" aria-label="Photo of a joyful man in a dark blazer celebrating with raised fists"></div>

<div class="band abs"><span>NOT A LIFELONG PROJECT</span><span>OR</span><span>YEARS OF THERAPY</span></div>

<h2 class="section-title abs">CHANGE BEGINS TODAY WITH OUR MASTER PRACTITIONER</h2>
<div class="intro abs">
  <p>Our clients experience their desired instant &amp; permanent transformation, emerging from our consultations ready to take on their world from a vastly different paradigm. At Tides Of Bloom, our Master Practitioner will inspire you, shifting your perspective &amp; facilitating your mind with the freedom to realise your dreams</p>
  <p><span class="hl">Join Alan Mercer, Ruth Danvers, P.L. Hartwell, Owen Strand, Leo Farrow,</span> Nina Calloway and hundreds of thousands of others who are achieving the life changing, consistent results you are dreaming of now.</p>
</div>
<div class="rule2 abs"></div>
<div class="testi-title abs">Testimonials</div>
<div class="arrows abs"><span>&#9664;</span><span>&#9654;</span></div>

<div class="testi abs" style="left:195px">
  <div class="avatar" role="img" aria-label="Client portrait"></div>
  <div class="name">MARK DOYLE ...</div>
  <div class="quote">Brilliant support by CoinHarbor who managed to recover an incorrect payment I ...</div>
  <div class="time">about 10 minutes ago</div>
</div>
<div class="testi abs" style="left:492px">
  <div class="avatar" role="img" aria-label="Client portrait"></div>
  <div class="name">ANN PRATT</div>
  <div class="quote">Excellent service, excellent team, they are so helpful.</div>
  <div class="time">about 2 hours ago</div>
</div>
<div class="testi abs" style="left:758px">
  <div class="avatar" role="img" aria-label="Client portrait"></div>
  <div class="name">ANN PRATT</div>
  <div class="quote">Excellent service, excellent team, they are so helpful.</div>
  <div class="time">about 2 hours ago</div>
</div>

<footer class="footer abs"></footer>
<div class="f-contact abs">Contact Us<small>418 Harbor Lane<br>Bayview, CA 90012</small></div>
<div class="socials abs"><span></span><span></span><span></span><span></span></div>
<div class="f-call abs"><div class="l">CALL TOLL-FREE</div><div class="n">1-800-555-0137</div></div>
<div class="f-rule abs"></div>
<div class="copyright abs">© 2013 tidesofbloom.biz All Rights Reserved &nbsp;| &nbsp;Disclaimer &nbsp;| &nbsp;Terms and Conditions</div>
</body>
</html>
```